Hi,

I would like to have a invitation made for a party. exactly like the picture in the link below.

http://pinboardia.example/pin/730215948361027459/

However, Please change the colors into fun/ girly feeling. font can be different and size of the card should be the same

Name of the girl: RINA
What: Bachelorette Party
Where:TOLO Boat
Dubai Coral Quay Sailing Club
When:7th of February 2013

No RSVP required. (so no need to put it)

```html
<!DOCTYPE html>
<html lang="en">
<head>
<meta charset="utf-8">
<title>Bachelorette Party Invitation – Rina</title>
<link rel="stylesheet" href="https://fonts.googleapis.com/css2?family=Anton&family=Open+Sans:wght@400;600;700&display=swap">
<style>
  :root {
    --violet-deep: #8e1f8c;
    --violet-mid: #a8208f;
    --magenta: #cf1f8f;
    --magenta-bright: #e4187f;
    --orange-light: #ffa51f;
    --orange-deep: #f2641c;
    --white: #ffffff;
    --ring-blue: #86d3f0;
    --ring-peach: #f7b9a4;
    --skin: #f3c9a5;
    --dress-lime: #d9ea4c;
    --hair-dark: #3a1a14;
    --hair-blond: #f7ecb8;
    --shorts-blue: #c4e6f3;
    --balloon-pink: #ff8fc8;
    --balloon-yellow: #ffe04a;
  }
  html, body {
    margin: 0;
    padding: 0;
    overflow: hidden;
  }
  .invitation {
    position: relative;
    width: 848px;
    height: 1200px;
    overflow: hidden;
    background: radial-gradient(circle at 52% 45%, var(--magenta) 0%, var(--violet-mid) 50%, var(--violet-deep) 100%);
    font-family: "Open Sans", Arial, sans-serif;
    color: var(--white);
  }
  .invitation p,
  .invitation h1 { margin: 0; }
  .decor {
    position: absolute;
    inset: 0;
    width: 848px;
    height: 1200px;
  }
  .heading {
    position: absolute;
    left: 0;
    top: 82px;
    width: 848px;
    text-align: center;
  }
  .heading__title {
    display: inline-block;
    font-family: "Anton", Impact, sans-serif;
    font-weight: 400;
    font-size: 62px;
    line-height: 1;
    letter-spacing: 3px;
    padding-left: 3px;
    transform: scaleX(1.3);
  }
  .heading__sub {
    display: block;
    font-weight: 600;
    font-size: 46px;
    line-height: 1;
    letter-spacing: 34px;
    padding-left: 86px;
    margin-top: 8px;
  }
  .details {
    position: absolute;
    left: 0;
    top: 210px;
    width: 900px;
    text-align: center;
    font-weight: 700;
    font-size: 26px;
    line-height: 32px;
  }
  .details__venue {
    display: block;
    font-size: 30px;
    line-height: 42px;
  }
  .date {
    position: absolute;
    left: 287px;
    top: 501px;
    width: 270px;
    text-align: center;
    font-size: 36px;
    line-height: 42px;
  }
  .date strong { font-weight: 700; }
  .art { position: absolute; }
  .art--balloons {
    left: 694px;
    top: 38px;
    width: 154px;
    height: 218px;
    border-radius: 50% 40% 45% 55%;
    background: radial-gradient(circle at 35% 35%, var(--balloon-yellow) 0%, var(--balloon-pink) 40%, var(--ring-blue) 72%, rgba(160,230,120,0) 100%);
    opacity: 0.9;
  }
  .art--guest-left {
    left: 120px;
    top: 730px;
    width: 400px;
    height: 470px;
    border-radius: 55% 45% 0 0 / 35% 35% 0 0;
    background: linear-gradient(160deg, var(--hair-dark) 0%, var(--skin) 24%, var(--dress-lime) 55%, var(--skin) 100%);
  }
  .art--guest-right {
    left: 545px;
    top: 590px;
    width: 290px;
    height: 610px;
    border-radius: 50% 50% 30% 30% / 22% 22% 0 0;
    background: linear-gradient(170deg, var(--hair-blond) 0%, var(--skin) 22%, var(--shorts-blue) 38%, var(--skin) 56%, var(--skin) 100%);
  }
</style>
</head>
<body>
<main class="invitation">

  <svg class="decor" viewBox="0 0 848 1200" aria-hidden="true">
    <defs>
      <radialGradient id="discGlow" cx="50%" cy="45%" r="55%">
        <stop offset="0%" stop-color="var(--orange-light)"/>
        <stop offset="100%" stop-color="var(--orange-deep)"/>
      </radialGradient>
      <path id="ribbonArc" d="M288 650 A175 175 0 0 1 543 416"/>
      <path id="ribbonBaseline" d="M294 646 A167 167 0 0 1 538 422"/>
    </defs>

    <g class="decor__rings" fill="none" stroke-width="3">
      <circle cx="150" cy="569" r="47" stroke="var(--white)"/>
      <circle cx="200" cy="600" r="50" stroke="var(--ring-peach)"/>
      <circle cx="144" cy="650" r="65" stroke="var(--ring-blue)"/>
      <circle cx="50" cy="571" r="18" stroke="var(--white)"/>
      <circle cx="141" cy="737" r="28" stroke="var(--ring-blue)"/>
    </g>
    <g class="decor__dots">
      <circle cx="754" cy="525" r="10" fill="var(--white)"/>
      <circle cx="812" cy="540" r="15" fill="var(--ring-blue)"/>
      <circle cx="845" cy="256" r="4" fill="var(--white)"/>
    </g>
    <g class="decor__streaks" stroke="var(--white)" stroke-width="3" fill="none">
      <line x1="0" y1="700" x2="90" y2="1200"/>
      <line x1="0" y1="760" x2="60" y2="1200"/>
      <line x1="10" y1="680" x2="120" y2="1200"/>
      <line x1="0" y1="860" x2="30" y2="1200"/>
      <path d="M0 900 Q200 835 540 825" stroke-width="4"/>
    </g>

    <circle class="date-disc" cx="431" cy="550" r="160" fill="url(#discGlow)"/>
    <use href="#ribbonArc" fill="none" stroke="var(--magenta-bright)" stroke-width="30"/>
    <text font-family="Open Sans, Arial, sans-serif" font-size="20" letter-spacing="5" fill="var(--white)">
      <textPath href="#ribbonBaseline" startOffset="2%">YOU ARE SPECIALLY INVITED</textPath>
    </text>
  </svg>

  <h1 class="heading">
    <span class="heading__title">BACHELORTTE</span>
    <span class="heading__sub">PARTY</span>
  </h1>

  <p class="details">
    Name of the girl: RINA<br>
    What: Bachelorette Party<br>
    Where:TOLO Boat
    <span class="details__venue">Dubai Coral Quay Sailing Club</span>
  </p>

  <p class="date">ON <strong>7th</strong><br>of <strong>February</strong><br>2013.</p>

  <div class="art art--balloons" role="img" aria-label="Cluster of colourful party balloons"></div>
  <div class="art art--guest-left" role="img" aria-label="Illustration of a dark-haired party girl in a lime heart-print dress dancing"></div>
  <div class="art art--guest-right" role="img" aria-label="Illustration of a blonde party girl in blue shorts dancing"></div>

</main>
</body>
</html>
```